"Beyond Marrow Cay" Fictional Book Cover

BEYOND MARROW CAY
By: Dale Pruitt

Here's the intro .

"It had been nearly forty years since Ted Larraby last went to the island from where he was raised. Three months earlier he never would have thought about ever coming back. But life is weird. Things happen quickly and plans change, especially when your very life is at stake. The reason he was going back wasn’t to see old friends...no, no, no. They’re all dead. Of all the kids he grew up with on the island who moved off, he’s the only one still alive. Why?"

Pretty much all just a Lumeno book, by the way.

Target Market(s)

fiction readers

Requirements
Must have
• Somewhat of a dark, mysterious cover is what I'd like to see. Use your imagination. I've never written a fiction book before so I'm very open to ideas

Needs to have my name, DALE PRUITT at the bottom. like my other books, all of which are non-fiction
Nice to have
• Mysterious is what I'm looking for. NOT A HORROR story though. More a guy who left the island years ago, but is being called back to escape the rat race of modern, consumerist culture.

Please remember this NEEDS to jump out as a thumbnail on Bookvale as people are browsing. Mainly the WORDS need to stick out. Lighter words on a say a blue background.

If you want to try to use the attached pic, or something like this, to reflect an island in the cover, that'd be good.

I've also uploaded a couple images I purchased from Pixelcrate, hopefully you can make something work with these.

```html
<!DOCTYPE html>
<html lang="en">
<head>
<meta charset="utf-8">
<title>Beyond Marrow Cay — Dale Pruitt</title>
<link rel="stylesheet" href="https://fonts.googleapis.com/css2?family=Barlow+Condensed:wght@600;700&family=Jost:wght@300&display=swap">
<style>
  :root {
    --sky-top: #0d2b5c;
    --sky-mid: #4f7fb1;
    --sky-low: #9cc6e6;
    --sky-haze: #bcd8ec;
    --title: #ffffff;
    --author: #2e508c;
    --hill: #0c100e;
  }
  html, body {
    margin: 0;
    padding: 0;
    width: 790px;
    height: 1200px;
    overflow: hidden;
    background: var(--sky-top);
  }
  .cover {
    position: relative;
    width: 790px;
    height: 1200px;
    overflow: hidden;
  }
  .cover__sky {
    position: absolute;
    inset: 0;
    background: linear-gradient(180deg,
      var(--sky-top) 0%,
      var(--sky-mid) 40%,
      var(--sky-low) 70%,
      var(--sky-haze) 100%);
  }
  .cover__hillside {
    position: absolute;
    right: -60px;
    bottom: -120px;
    width: 620px;
    height: 330px;
    background: radial-gradient(ellipse at 75% 75%,
      var(--hill) 0%, var(--hill) 48%, rgba(12,16,14,0.55) 62%, rgba(12,16,14,0) 72%);
  }
  .cover__title {
    position: absolute;
    left: 0;
    top: 0;
    width: 790px;
    height: 760px;
  }
  .title__lead {
    font-family: "Jost", sans-serif;
    font-weight: 300;
    font-size: 148px;
    fill: var(--title);
  }
  .title__main {
    font-family: "Barlow Condensed", sans-serif;
    font-weight: 700;
    fill: var(--title);
  }
  .cover__author {
    position: absolute;
    right: 66px;
    top: 828px;
    margin: 0;
    font-family: "Barlow Condensed", sans-serif;
    font-weight: 600;
    font-size: 64px;
    line-height: 1;
    color: var(--author);
  }
</style>
</head>
<body>
  <main class="cover">
    <div class="cover__sky" role="img" aria-label="Clear evening sky fading from deep blue to pale blue"></div>
    <div class="cover__hillside" role="img" aria-label="Dark silhouette of an island hillside with a lone house at its crest"></div>

    <svg class="cover__title" viewBox="0 0 790 760" aria-label="Beyond Marrow Cay">
      <text class="title__lead" x="68" y="180" textLength="656" lengthAdjust="spacing">BEYOND</text>
      <text class="title__main" x="68" y="460" font-size="354" textLength="656" lengthAdjust="spacingAndGlyphs">MARROW</text>
      <text class="title__main" x="68" y="736" font-size="326" textLength="656" lengthAdjust="spacing">CAY</text>
    </svg>

    <p class="cover__author">Dale Pruitt</p>
  </main>
</body>
</html>
```